Brackwell Immigration Law

We need a web design for our existing company www.brackwellcounselpartners.co.uk. We are an immigration consultancy. The final design should communicate professionalism, integrity and affordability.

Industry/Entity Type

It Company

Logo Text

Brackwell Counsel Partners

Number of Pages Required

5+ page

Font styles to use
Serif

Requirements
Must have
• I want to have the same silhouette logo but something different in positioning..
Nice to have
• Please have a look at these websites:
• https://www.tenderpathguide.co.uk/visa_uk/
• http://www.moorgatelegal.co.uk/
• http://www.quillfieldcounsel.org/index.php
• www.brackwellcounselpartners.co.uk

```html
<!DOCTYPE html>
<html lang="en">
<head>
<meta charset="utf-8">
<title>Brackwell Immigration Law</title>
<link href="https://fonts.googleapis.com/css2?family=Open+Sans:wght@300;400;600;700&display=swap" rel="stylesheet">
<style>
:root{
  --red:#9c1c20;
  --ink:#333333;
  --muted:#8a8a8a;
  --light:#f0f0f0;
  --panel:#e9e9e9;
  --footer:#2a2a2a;
  --footer-base:#1d1d1d;
  --white:#ffffff;
}
*{box-sizing:border-box;margin:0;padding:0}
html,body{width:1200px;height:2608px;overflow:hidden;background:var(--white)}
body{font-family:"Open Sans",Arial,sans-serif;color:var(--ink);position:relative}
a{color:inherit;text-decoration:none}

/* header */
.site-header{height:112px;display:flex;align-items:center;justify-content:space-between;padding:0 100px;border-bottom:1px solid #e4e4e4}
.brand-name{font-size:25px;font-weight:700;color:var(--ink);line-height:1.1}
.brand-name span{color:var(--red)}
.brand-tag{font-size:16px;color:var(--muted);margin-top:2px}
.main-nav{display:flex;align-items:center;gap:6px}
.main-nav a{font-size:13px;font-weight:600;text-transform:uppercase;padding:14px 18px;color:var(--ink)}
.main-nav a.active{background:var(--red);color:var(--white)}
.main-nav a.search{padding:14px 10px;display:flex;align-items:center}

/* hero */
.hero{position:relative;height:620px;background:linear-gradient(100deg,#dfe3e6 0%,#b9c2c9 35%,#5c6773 65%,#39424d 100%)}
.hero-copy{position:absolute;left:100px;top:200px}
.hero-copy .lead{font-size:48px;font-weight:300;color:var(--white);letter-spacing:1px}
.hero-copy .big{font-size:96px;font-weight:700;color:var(--red);line-height:1;letter-spacing:2px}
.hero-arrows{position:absolute;left:100px;bottom:24px;display:flex;gap:4px}
.hero-arrows span{width:30px;height:30px;background:rgba(0,0,0,.45);display:flex;align-items:center;justify-content:center}

/* welcome */
.welcome{text-align:center;padding-top:60px;height:204px}
.section-title{font-size:40px;font-weight:300;line-height:52px;letter-spacing:1px;text-transform:uppercase;color:var(--ink)}
.section-title em{font-style:normal;color:var(--red)}
.welcome p{width:700px;margin:16px auto 0;font-size:13px;color:var(--muted);line-height:21px}

.features{display:flex;gap:36px;padding:0 100px;height:352px}
.feature{flex:1;height:352px;background:var(--panel);text-align:center;padding-top:46px}
.feature.highlight{background:var(--red);color:var(--white)}
.feature h3{font-size:16px;font-weight:700;margin-top:30px;text-transform:uppercase}
.feature p{width:230px;margin:16px auto 0;font-size:12px;line-height:1.6;color:#777}
.feature.highlight p{color:#f1d6d7}

/* practice areas */
.practice{padding:0 100px;margin-top:76px;position:relative;height:318px}
.practice .section-title{text-align:center}
.practice-arrows{position:absolute;right:92px;top:11px;display:flex;gap:6px}
.practice-arrows span{width:30px;height:30px;background:#cfcfcf;display:flex;align-items:center;justify-content:center}
.areas{display:flex;gap:16px;margin-top:34px}
.area{flex:1;position:relative;height:230px}
.area .photo{height:186px}
.area .caption{position:absolute;left:16px;right:16px;bottom:0;min-height:52px;background:#222;color:var(--white);font-size:13px;font-weight:600;text-align:center;padding:8px;text-transform:uppercase;line-height:18px;display:flex;align-items:center;justify-content:center}

/* news */
.news{position:absolute;left:0;top:1728px;width:1200px;height:512px;background:var(--light);padding:100px 100px 0}
.news .section-title{text-align:center;font-size:34px;line-height:44px}
.news-cols{display:flex;gap:60px;margin-top:48px}
.news-col{flex:1}
.news-col h4{font-size:15px;font-weight:700;text-transform:uppercase;padding-bottom:10px;border-bottom:1px solid #d5d5d5}
.news-item{margin-top:18px}
.news-item time{display:block;font-size:11px;color:var(--red);font-weight:600}
.news-item h5{font-size:12px;font-weight:700;margin-top:3px;text-transform:uppercase}
.news-item p{font-size:12px;color:#777;margin-top:6px;line-height:1.5}

/* footer */
.site-footer{position:absolute;left:0;top:2240px;width:1200px;height:368px;background:var(--footer);color:#cfcfcf;padding:56px 100px 0}
.footer-cols{display:flex}
.footer-cols h4{font-size:15px;font-weight:700;color:var(--white);text-transform:uppercase;margin-bottom:16px}
.footer-links{width:240px}
.footer-links li{list-style:none;font-size:12px;line-height:1.75;text-transform:uppercase}
.newsletter{width:430px}
.newsletter p{font-size:12px;margin-bottom:12px}
.newsletter .field{width:240px;height:30px;background:var(--white);margin-bottom:10px;font-size:11px;color:#999;padding:7px 10px}
.newsletter .btn{display:inline-block;background:var(--red);color:var(--white);font-size:12px;font-weight:700;padding:7px 16px;text-transform:uppercase}
.contact-block{font-size:12px;line-height:1.7}
.socials{display:flex;justify-content:center;gap:14px;margin-top:26px}
.socials span{width:20px;height:20px;border-radius:50%;background:#9a9a9a}
.regulated{text-align:center;font-size:12px;margin-top:22px;color:#bdbdbd}
.base-bar{position:absolute;left:0;bottom:0;width:1200px;height:48px;background:var(--footer-base);text-align:center;font-size:11px;color:#8f8f8f;padding-top:16px}
</style>
</head>
<body>

<header class="site-header">
  <div class="brand">
    <div class="brand-name">Brackwell <span>Counsel Partners</span></div>
    <div class="brand-tag">Immigration Law</div>
  </div>
  <nav class="main-nav">
    <a class="active" href="#">Home</a>
    <a href="#">About Us</a>
    <a href="#">Join Us</a>
    <a href="#">Contact</a>
    <a href="#">Blog</a>
    <a class="search" href="#" aria-label="Search">
      <svg width="16" height="16" viewBox="0 0 16 16"><circle cx="6.5" cy="6.5" r="5" fill="none" stroke="#333" stroke-width="2"/><line x1="10.5" y1="10.5" x2="15" y2="15" stroke="#333" stroke-width="2"/></svg>
    </a>
  </nav>
</header>

<section class="hero" role="img" aria-label="Photograph of two lawyers in suits reviewing documents at a desk">
  <div class="hero-copy">
    <div class="lead">WE ARE IMMIGRATION</div>
    <div class="big">LAWYERS</div>
  </div>
  <div class="hero-arrows">
    <span><svg width="10" height="12" viewBox="0 0 10 12"><path d="M8 1 2 6l6 5" fill="none" stroke="#fff" stroke-width="2"/></svg></span>
    <span><svg width="10" height="12" viewBox="0 0 10 12"><path d="M2 1l6 5-6 5" fill="none" stroke="#fff" stroke-width="2"/></svg></span>
  </div>
</section>

<section class="welcome">
  <h2 class="section-title">Welcome to <em>Brackwell</em></h2>
  <p>We guide families, workers and students through every stage of the UK visa process with clear advice and fair, fixed fees for each application we handle.</p>
</section>

<section class="features">
  <article class="feature highlight">
    <svg width="90" height="70" viewBox="0 0 90 70"><circle cx="45" cy="18" r="10" fill="#fff"/><path d="M30 44c0-10 7-16 15-16s15 6 15 16z" fill="#fff"/><circle cx="12" cy="40" r="7" fill="#fff"/><circle cx="78" cy="40" r="7" fill="#fff"/><circle cx="45" cy="62" r="7" fill="#fff"/><line x1="19" y1="40" x2="32" y2="38" stroke="#fff" stroke-width="3"/><line x1="71" y1="40" x2="58" y2="38" stroke="#fff" stroke-width="3"/><line x1="45" y1="44" x2="45" y2="55" stroke="#fff" stroke-width="3"/></svg>
    <h3>Our Team</h3>
    <p>Experienced advisers who listen first, explain each option plainly and stay with you until a decision.</p>
  </article>
  <article class="feature">
    <svg width="90" height="70" viewBox="0 0 90 70"><g fill="#9c1c20"><circle cx="34" cy="30" r="14"/><circle cx="62" cy="48" r="10"/><g stroke="#9c1c20" stroke-width="6"><line x1="34" y1="8" x2="34" y2="52"/><line x1="12" y1="30" x2="56" y2="30"/><line x1="18" y1="14" x2="50" y2="46"/><line x1="50" y1="14" x2="18" y2="46"/><line x1="62" y1="33" x2="62" y2="63"/><line x1="47" y1="48" x2="77" y2="48"/></g></g><circle cx="34" cy="30" r="6" fill="#e9e9e9"/><circle cx="62" cy="48" r="4" fill="#e9e9e9"/></svg>
    <h3>Services</h3>
    <p>Visa applications, appeals, settlement and sponsor licences handled with care at a clear, fixed price.</p>
  </article>
  <article class="feature">
    <svg width="90" height="70" viewBox="0 0 90 70"><path d="M45 68C33 50 26 40 26 27a19 19 0 0 1 38 0c0 13-7 23-19 41z" fill="#9c1c20"/><circle cx="45" cy="27" r="7" fill="#e9e9e9"/></svg>
    <h3>Contact Us</h3>
    <p>London Office<br>Brackwell Counsel Partners<br>14 Harrowgate Row, London W8 5SA</p>
  </article>
</section>

<section class="practice">
  <h2 class="section-title">Our <em>Immigration Law</em></h2>
  <div class="practice-arrows">
    <span><svg width="10" height="12" viewBox="0 0 10 12"><path d="M8 1 2 6l6 5" fill="none" stroke="#fff" stroke-width="2"/></svg></span>
    <span><svg width="10" height="12" viewBox="0 0 10 12"><path d="M2 1l6 5-6 5" fill="none" stroke="#fff" stroke-width="2"/></svg></span>
  </div>
  <div class="areas">
    <div class="area"><div class="photo" role="img" aria-label="Photograph of a smiling client" style="background:linear-gradient(160deg,#c9746a,#8d3b36)"></div><div class="caption">Entry Clearance /<br>Dependant Visas</div></div>
    <div class="area"><div class="photo" role="img" aria-label="Photograph of a judge's gavel on a desk" style="background:linear-gradient(160deg,#6e6257,#2f2822)"></div><div class="caption">Immigration Appeals</div></div>
    <div class="area"><div class="photo" role="img" aria-label="Photograph of two people signing papers" style="background:linear-gradient(160deg,#d8cfc4,#8e7d6c)"></div><div class="caption">Settlement Applications<br>ILR</div></div>
    <div class="area"><div class="photo" role="img" aria-label="Photograph of a passport in a hand" style="background:linear-gradient(160deg,#5a6f8a,#1f2c3c)"></div><div class="caption">Domestic Workers Visa</div></div>
  </div>
</section>

<section class="news">
  <h2 class="section-title">News &amp; Publications</h2>
  <div class="news-cols">
    <div class="news-col">
      <h4>Company News</h4>
      <div class="news-item"><time>May 14, 2015 at 7:00 PM</time><h5>Court listings unavailable until Friday morning</h5><p>Dear clients, please be advised that the online booking portal will not be available until then.</p></div>
      <div class="news-item"><time>February 13, 2015 at 10:02 AM</time><h5>Appeal deadlines extended for 2015</h5><p>New guidance gives applicants more time, offering wider options for late submissions.</p></div>
    </div>
    <div class="news-col">
      <h4>Breaking News</h4>
      <div class="news-item"><time>May 14, 2015 at 1:00 PM</time><h5>Sponsor licence rules updated for employers</h5><p>LONDON (June 28) – Employers holding licences must review records by Friday at noon.</p></div>
      <div class="news-item"><time>July 02, 2015 at 3:00 PM</time><h5>Overseas workers travel guidance revised</h5><p>By staff writer LONDON, June 28 – Updated entry checks apply to new arrivals.</p></div>
    </div>
  </div>
</section>

<footer class="site-footer">
  <div class="footer-cols">
    <div class="footer-links">
      <h4>Brackwell</h4>
      <ul><li>Home</li><li>About Us</li><li>Join Us</li><li>Contact</li><li>Blog</li></ul>
    </div>
    <div class="newsletter">
      <h4>Sign to Newsletter</h4>
      <p>Join our mailing list for visa updates.</p>
      <div class="field">Name</div>
      <div class="field">Email</div>
      <span class="btn">Subscribe</span>
    </div>
    <div class="contact-block">
      <h4>Contact Us</h4>
      London Office: Brackwell Counsel Partners<br>
      14 Harrowgate Row, London W8 5SA<br>
      Tel: +44 020 7946 0182<br>
      Fax: +44 020 7946 0183<br>
      info@brackwellcounselpartners.co.uk
    </div>
  </div>
  <div class="socials" aria-hidden="true"><span></span><span></span><span></span><span></span><span></span></div>
  <p class="regulated">Regulated by the immigration services regulator, reference F201500123, and authorised to practise in England and Wales.</p>
  <div class="base-bar">© 2015 Brackwell Counsel Partners. All rights reserved.</div>
</footer>

</body>
</html>
```